依頼詳細
不動産物件情報の冊子の表紙デザインです。春号らしいイメージと、簡単には捨てられないインパクトのあるデザインをお願いします。
※参考まで前号(冬号)の表紙を添付いたします
会社WEB:http://meridel-works.jp/
※必ずしも、前号のイメージにとらわれる必要はありません
記載項目
タイトル「物件情報 2020 春号」 会社ロゴ:添付参照 10周年記念タイトル:添付参照
希望イメージ
シンプル 複雑
単色 カラフル
暗い 明るい
日常 高級
遊び心 厳粛
未来的 伝統的
女性的 男性的
希望する色
設定なし
納品ファイル
• 高解像度JPG (.jpg)
• イラストレーター形式 (.ai)
補足説明
四半期に一度発行予定ですので、継続して発行して行きます
■ 選んだ理由

最終選考の4案中、一番投票が多かったです。
春の都会をうまく表現したデザインで、表紙にふさわしいと決定しました

■ 提案者全員のお礼・コメント

ご提案いただいた、多数の皆様、誠にありがとうございます。
また、次号の募集にもご参加いただければ幸いです

```html
<!DOCTYPE html>
<html lang="ja">
<head>
<meta charset="utf-8">
<title>物件情報 2020春号</title>
<link href="https://fonts.googleapis.com/css2?family=Shippori+Mincho:wght@500;700&family=Noto+Sans+JP:wght@500;700&family=Cormorant+Garamond:wght@600&display=swap" rel="stylesheet">
<style>
  :root {
    --blossom: #f0a3bd;
    --blossom-light: #f9d7e2;
    --spring-green: #b5d37a;
    --paper: #ffffff;
    --title-brown: #6b4a24;
    --title-gold: #b08a3e;
    --issue-pink: #e57ea0;
    --ink: #3a3230;
    --brand-green: #7bb04a;
    --city-grey: #8e8e7c;
    --badge-gold: #c9a24a;
  }
  * { margin: 0; padding: 0; box-sizing: border-box; }
  html, body { width: 846px; height: 1200px; overflow: hidden; }
  body {
    position: relative;
    background: linear-gradient(180deg, var(--blossom) 0%, #eab7bf 55%, var(--spring-green) 100%);
    font-family: "Noto Sans JP", sans-serif;
  }
  .cover-panel {
    position: absolute;
    left: 62px; right: 62px; top: 0; bottom: 0;
    background: linear-gradient(180deg, var(--paper) 0%, var(--paper) 30%, #fdf0f3 60%, #eee9d2 85%, #dde7bd 100%);
  }
  .cover-title {
    position: absolute;
    top: 28px; left: 0; width: 100%;
    text-align: center;
    font-family: "Shippori Mincho", serif;
    font-weight: 700;
    font-size: 104px;
    letter-spacing: 44px;
    padding-left: 44px;
    color: var(--title-brown);
    background: linear-gradient(180deg, var(--title-gold), var(--title-brown));
    -webkit-background-clip: text;
    background-clip: text;
    -webkit-text-fill-color: transparent;
  }
  .issue-label {
    position: absolute;
    top: 168px; left: 0; width: 100%;
    text-align: center;
    font-size: 26px;
    letter-spacing: 9px;
    padding-left: 9px;
    color: var(--issue-pink);
    font-weight: 500;
  }
  .anniversary-badge {
    position: absolute;
    left: 338px; top: 238px;
    width: 170px; height: 116px;
    border-radius: 58px;
    background: radial-gradient(circle at 50% 40%, #ecd590, var(--badge-gold) 70%);
  }
  .anniversary-message {
    position: absolute;
    left: 488px; top: 388px;
    writing-mode: vertical-rl;
    font-family: "Shippori Mincho", serif;
    font-weight: 700;
    font-size: 30px;
    line-height: 1.45;
    letter-spacing: 3px;
    color: var(--ink);
  }
  .anniversary-message .tcy { text-combine-upright: all; }
  .petal-drift {
    position: absolute;
    left: 62px; right: 62px; top: 200px; height: 640px;
    background: radial-gradient(ellipse at 30% 40%, rgba(240,163,189,0.22), transparent 60%),
                radial-gradient(ellipse at 80% 60%, rgba(240,163,189,0.18), transparent 55%);
  }
  .brand {
    position: absolute;
    top: 720px; left: 0; width: 100%;
    text-align: center;
  }
  .brand-mark {
    display: block;
    width: 82px; height: 82px;
    margin: 0 auto 10px;
    border-radius: 50%;
    background: var(--brand-green);
  }
  .brand-name {
    font-family: "Cormorant Garamond", serif;
    font-weight: 600;
    font-size: 40px;
    letter-spacing: 2px;
    color: var(--ink);
  }
  .cityscape {
    position: absolute;
    left: 62px; right: 62px; bottom: 0; height: 330px;
    background: linear-gradient(180deg, rgba(142,142,124,0) 0%, rgba(142,142,124,0.55) 30%, rgba(122,128,96,0.8) 100%);
  }
</style>
</head>
<body>
  <div class="cover-panel"></div>
  <div class="petal-drift" role="img" aria-label="舞い散る桜の花びら"></div>

  <h1 class="cover-title">物件情報</h1>
  <p class="issue-label">2020春号Spring</p>

  <div class="anniversary-badge" role="img" aria-label="10周年記念エンブレム"></div>

  <p class="anniversary-message">
    株式会社メリデルは、<br>
    おかげさまで<br>
    <span class="tcy">10</span>周年を迎えました
  </p>

  <div class="brand">
    <span class="brand-mark"></span>
    <span class="brand-name">Meridel</span>
  </div>

  <div class="cityscape" role="img" aria-label="春の街並みのビル群のシルエット"></div>
</body>
</html>
```